Flyer-Design für Prozessfinanzierungsfirma
Zielgruppe
Wir sind eine Prozessfinanzierungsfirma. im Versicherungsbereich die größte Österreichs mit mehr als 50.000 Klienten und unser neues Projekt ist die Prozessfinanzierung von Patienten die durch einen Kunstfehler (Fehler von Ärzten) auf Schadenersatz klagen wollen aber nicht die Finanziellen Möglichkeiten haben.
Aufgabenstellung
Folder soll eine DIN A4 Doppelseite sein (also 4 A4 Seiten)
plus extra ein A4 Einlage Blatt Fragebogen fix vorgegebene Fragen.
#604132 Dieser Folder ist für die gleiche Firma im Bereich Versicherungen
www.heilirrtum-beispiel.at. TEXTE und DESIGN - FARBEN und INHALTE von dieser Homepage übernehmen
die Seite www.schutzbrief-muster.at ist die gleiche Prozessfinanzierungsfirma - hier gibt es bereits einen Folder. Ich lade diesen hoch...
Diese Fragen sind unbedingt 1:1 zu übernehmen für das Einlageblatt :
o Was waren meine Erkrankungen vor der Behandlung, inkl. Dauermedikation?
o Warum ging ich zum Arzt?
o Was hat mir der Arzt empfohlen?
o Wurde ich über die unterschiedlichen Behandlungsmöglichkeiten aufgeklärt?
o Was wollte ich haben?
o Was wurde gemacht?
o Was hat der Arzt aus meiner Sicht falsch gemacht?
o Was wurde als weiterer Behandlungsweg empfohlen?
o Habe ich den Arzt mit meinem Problem konfrontiert?
o Wie hat mein Arzt darauf reagiert?
o Was ist jetzt genau schlechter als vorher?
Bei dem A4 Einlageblatt sollen auf der Vorderseite und der halben Rückseite diese Fragen mit entsprechendem Platz für den Text zum ausfüllen erscheinen und die untere Hälfte der 2. Seite mit einem kurzen Slogan nochmal auf unsere Leistung aufmerksam machen - ein Feld in Kreditkartengrösse für den Empfehlungsbgeber weiss zum einkleben einer Karte freibleiben und die Firmendaten (siehe Homepage) mit Anschrift, Telefonnummer und e-mailadresse angegeben sein

```html
<!DOCTYPE html>
<html lang="de">
<head>
<meta charset="utf-8">
<title>Fragebogen – Einlageblatt Rückseite</title>
<link href="https://fonts.googleapis.com/css2?family=PT+Sans:wght@400;700&family=Rochester&display=swap" rel="stylesheet">
<style>
  :root {
    --backdrop: #e4e1dd;
    --paper: #f1f1f3;
    --band: #ffffff;
    --ink: #3a3a3a;
    --dash: #c79a9d;
    --maroon-dark: #7c1c22;
    --maroon-mid: #9b3a40;
    --maroon-light: #c68e91;
    --white: #ffffff;
  }
  html, body {
    margin: 0;
    width: 1200px;
    height: 797px;
    overflow: hidden;
    background: var(--backdrop);
    font-family: "PT Sans", Arial, sans-serif;
  }
  .sheet {
    position: absolute;
    left: 331px;
    top: 18px;
    width: 537px;
    height: 760px;
    background: var(--paper);
    overflow: hidden;
    box-shadow: 0 4px 18px rgba(0,0,0,.18);
  }
  .question {
    position: absolute;
    left: 18px;
    right: 0;
    height: 58px;
  }
  .question__label {
    font-size: 11px;
    color: var(--ink);
    margin: 0;
    white-space: nowrap;
  }
  .question__field {
    position: absolute;
    left: 22px;
    right: 18px;
    top: 15px;
    height: 40px;
    background: var(--band);
    border-radius: 0 20px 20px 0;
    padding: 7px 22px 0 8px;
    box-sizing: border-box;
  }
  .question__line {
    border-top: 1px dashed var(--dash);
    height: 10px;
  }
  .footer-band {
    position: absolute;
    left: 0;
    top: 0;
    width: 537px;
    height: 760px;
  }
  .slogan {
    position: absolute;
    left: 22px;
    top: 520px;
    margin: 0;
    font-family: "Rochester", "Brush Script MT", cursive;
    font-weight: 400;
    color: var(--white);
    font-size: 23px;
    line-height: 28px;
    transform: rotate(-7deg);
    transform-origin: left top;
    white-space: nowrap;
  }
  .slogan span { display: block; }
  .slogan span + span { padding-left: 18px; }
  .company {
    position: absolute;
    left: 36px;
    top: 612px;
    margin: 0;
    font-style: normal;
    color: var(--white);
    font-size: 10.5px;
    line-height: 14px;
  }
  .referral-card {
    position: absolute;
    left: 318px;
    top: 566px;
    width: 198px;
    height: 124px;
    background: var(--white);
    border-radius: 18px;
    text-align: center;
  }
  .referral-card__label {
    margin: 22px 0 0;
    font-size: 9px;
    font-weight: 700;
    color: var(--maroon-mid);
  }
</style>
</head>
<body>
  <main class="sheet">
    <section class="questionnaire">
      <div class="question" style="top:16px">
        <p class="question__label">7) Was hat der Arzt aus meiner Sicht falsch gemacht?</p>
        <div class="question__field"><div class="question__line"></div><div class="question__line"></div><div class="question__line"></div></div>
      </div>
      <div class="question" style="top:74px">
        <p class="question__label">8) Habe ich den Arzt mit meinem Problem konfrontiert? Wenn ja, wie hat er darauf reagiert?</p>
        <div class="question__field"><div class="question__line"></div><div class="question__line"></div><div class="question__line"></div></div>
      </div>
      <div class="question" style="top:132px">
        <p class="question__label">9) Was wurde als weiterer Behandlungsweg empfohlen?</p>
        <div class="question__field"><div class="question__line"></div><div class="question__line"></div><div class="question__line"></div></div>
      </div>
      <div class="question" style="top:190px">
        <p class="question__label">10) Wie hat mein Arzt darauf reagiert?</p>
        <div class="question__field"><div class="question__line"></div><div class="question__line"></div><div class="question__line"></div></div>
      </div>
      <div class="question" style="top:248px">
        <p class="question__label">11) Was ist jetzt genau schlechter als vorher?</p>
        <div class="question__field"><div class="question__line"></div><div class="question__line"></div><div class="question__line"></div></div>
      </div>
      <div class="question" style="top:306px">
        <p class="question__label">12) Gab es vor dieser Behandlung Erkrankungen/Operationen oder Dauermedikationen? Wenn ja, welche?</p>
        <div class="question__field"><div class="question__line"></div><div class="question__line"></div><div class="question__line"></div></div>
      </div>
      <div class="question" style="top:364px">
        <p class="question__label">13) Haben Sie schon eine Forderung gestellt? Wenn ja, durch wen und an wen? Welche Antwort erfolgte?</p>
        <div class="question__field"><div class="question__line"></div><div class="question__line"></div><div class="question__line"></div></div>
      </div>
    </section>

    <svg class="footer-band" viewBox="0 0 537 760" aria-hidden="true">
      <defs>
        <linearGradient id="bandGradient" x1="0" y1="1" x2="1" y2="0">
          <stop offset="0" stop-color="#7c1c22"/>
          <stop offset="0.5" stop-color="#c68e91"/>
          <stop offset="1" stop-color="#9b3a40"/>
        </linearGradient>
      </defs>
      <path d="M0 505 C 160 488, 340 458, 537 432 L537 760 L0 760 Z" fill="url(#bandGradient)"/>
    </svg>

    <h2 class="slogan">
      <span>Sichern Sie rechtzeitig Ihren Geldanspruch!</span>
      <span>Mit unseren spezialisierten Fachanwälten!</span>
    </h2>

    <address class="company">
      NK Prozessfinanzierung GmbH<br>
      FN 123456a<br>
      UID: ATU00000000<br>
      Musterplatz 12<br>
      1010 Wien<br>
      Tel: +43 (0)1/000 00 00<br>
      Fax: +43 (0)1/000 00 00-10<br>
      www.heilirrtum-beispiel.at<br>
      office@heilirrtum-beispiel.at
    </address>

    <div class="referral-card">
      <p class="referral-card__label">empfohlen von</p>
    </div>
  </main>
</body>
</html>
```